infographic - healing the addiction cycle

Please create a 3 slide infographic based on the three slides attached, as you can see they are builds on each other. I would love you to use pictures to complement the words and make it look beautiful. Please try to illustrate as much as possible i a looking for something really creative, clean and beautiful that articulates these concepts well.
My website is www.calmorbel.com.au so you can get an idea of branding and style.
This infographic will be used in training to teach new practitioners and clients how to heal their addictions.

Target Market(s)

Women aged 30 - 45

Industry/Entity Type

Professional Service

Font styles to use
Sans Serif

Colors

Designer to choose colors to be used in the design.

Requirements
Must have
• the blue color of my logo on it, i also like white
• Visual depictions not just words
• please look at my website to get an idea of style
Nice to have
• I would like it to be very clear, classy and as simple as possible
Should not have
• It needs to be neat not messy, symmetrical is better.

```html
<!DOCTYPE html>
<html lang="en">
<head>
<meta charset="utf-8">
<title>Healing the Addiction Cycle with OPH</title>
<link href="https://fonts.googleapis.com/css2?family=Poppins:wght@300;400;600;700&display=swap" rel="stylesheet">
<style>
  :root{
    --teal:#1ab4cf;
    --teal-light:#a9dff0;
    --teal-mid:#6fcbe4;
    --card:#f2f2f2;
    --ink:#444a4f;
    --white:#ffffff;
  }
  *{box-sizing:border-box;margin:0;padding:0}
  html,body{width:1200px;height:1000px;overflow:hidden;background:var(--white)}
  .canvas{position:relative;width:1200px;height:1000px;overflow:hidden;font-family:"Poppins",sans-serif;color:var(--ink)}
  .brand-mark{position:absolute;left:14px;top:184px;display:flex;align-items:center;gap:10px}
  .brand-mark .dot{width:42px;height:42px;border:2px solid var(--teal);border-radius:50%}
  .brand-mark .name{font-size:21px;font-weight:400;color:var(--teal)}
  .headline{position:absolute;left:0;top:250px;width:1200px;text-align:center;font-size:31px;font-weight:300;letter-spacing:3px;color:var(--teal)}
  .headline strong{font-weight:600}
  .step{position:absolute;background:var(--card);border-radius:10px;font-size:14.5px;line-height:1.27;text-align:center}
  .step p{margin:0}
  .step ul{list-style:none;text-align:left;color:var(--teal);font-size:12px;font-weight:600;line-height:1.25}
  .step li{position:relative;padding-left:12px}
  .step li::before{content:"•";position:absolute;left:0}
  .step-deny{left:198px;top:315px;width:344px;height:147px;padding:8px 26px}
  .step-deny ul{margin:4px 0 0 84px}
  .step-reaction{left:645px;top:318px;width:245px;height:140px;padding:6px 12px}
  .step-reaction ul{margin:4px 0 0 30px}
  .step-abuse{left:230px;top:492px;width:218px;height:140px;padding:26px 14px 0}
  .step-emotion{left:740px;top:493px;width:220px;height:140px;padding:8px 12px}
  .step-emotion ul{margin:4px 0 0 20px}
  .step-judge{left:494px;top:652px;width:220px;height:140px;padding:12px 22px 0}
  .reassure{position:absolute;left:478px;top:485px;width:248px;height:130px;background:var(--teal);color:var(--white);font-size:14.5px;font-weight:600;line-height:1.27;text-align:center;padding:18px 8px}
  .flow{position:absolute;left:0;top:0;z-index:2}
  .studio{position:absolute;right:22px;top:752px;font-size:40px;font-weight:300;color:var(--teal);letter-spacing:-1px;line-height:1.2}
</style>
</head>
<body>
<div class="canvas">
  <div class="brand-mark"><span class="dot"></span><span class="name">Open Path Healing</span></div>
  <h1 class="headline">HEALING THE ADDICTION CYCLE &nbsp;|&nbsp; <strong>WITH OPH</strong></h1>

  <section class="step step-deny">
    <p>Desire to respress or deny compounded by the physical, mental and emotional pain responsible becomes unbearable.</p>
    <ul><li>What is the emotion I am experiencing?</li><li>Feel where it is in the body</li><li>Turn it up</li><li>Release It</li></ul>
  </section>
  <section class="step step-reaction">
    <p>Physical and mental reaction to the emotional response</p>
    <ul><li>What is the emotion I am experiencing?</li><li>Feel where it is in the body</li><li>Turn it up</li><li>Release It</li></ul>
  </section>
  <section class="step step-abuse">
    <p>Commit self abuse<br>through addictive<br>behaviour e.g. drugs,<br>alcohol, food, gambling,<br>exercise etc.</p>
  </section>
  <div class="reassure">You don't need to worry that you've acted on the addition - at all points in the cycle there is something you can do to heal yourself from it.</div>
  <section class="step step-emotion">
    <p>Emotional Reaction<br>to self judgment</p>
    <ul><li>What is the emotion I am experiencing?</li><li>Feel where it is in the body</li><li>Turn it up</li><li>Release It</li></ul>
  </section>
  <section class="step step-judge">
    <p>Self Judgement Practice forgiveness and compassion for self. ie: I love you, I'm sorry, Please forgive me, Thank you</p>
  </section>

  <svg class="flow" width="1200" height="1000" viewBox="0 0 1200 1000" aria-hidden="true">
    <g fill="none" stroke="var(--teal)" stroke-width="16">
      <path d="M645 380 Q602 362 560 374"/>
      <path d="M440 462 Q437 484 428 496"/>
      <path d="M440 632 Q452 676 482 688"/>
      <path d="M714 690 Q742 676 750 652"/>
      <path d="M772 493 Q767 478 758 468"/>
    </g>
    <g fill="var(--teal)">
      <polygon points="530,382 558,358 564,396"/>
      <polygon points="418,516 410,490 442,500"/>
      <polygon points="506,698 482,674 476,708"/>
      <polygon points="758,626 736,650 768,656"/>
      <polygon points="748,448 732,472 766,464"/>
    </g>
    <path d="M170 324 Q150 340 140 338 L140 372 Q140 402 170 418 Q200 402 200 372 L200 338 Q190 340 170 324Z" fill="var(--teal-light)" stroke="var(--teal)" stroke-width="4"/>
    <path d="M170 340 Q158 350 152 350 L152 372 Q152 392 170 402 Z" fill="var(--teal)"/>
    <polygon points="203,490 212,522 244,510 226,538 244,556 214,558 218,592 198,568 176,596 178,562 150,556 172,538 160,508 188,522" fill="var(--teal-light)"/>
    <polygon points="202,506 208,528 230,520 218,540 230,552 210,553 212,576 198,560 182,578 184,556 166,552 182,540 174,520 192,530" fill="var(--teal)"/>
    <rect x="712" y="716" width="54" height="58" fill="var(--teal)"/>
    <rect x="708" y="706" width="62" height="14" fill="var(--teal-light)"/>
    <rect x="734" y="706" width="10" height="68" fill="var(--teal-light)"/>
    <path d="M739 706 Q724 688 716 698 Q716 706 739 706 Q754 688 762 698 Q762 706 739 706" fill="none" stroke="var(--teal-mid)" stroke-width="3"/>
    <path d="M979 580 L946 546 Q932 528 946 512 Q962 500 979 518 Q996 500 1012 512 Q1026 528 1012 546 Z" fill="var(--teal-light)" stroke="var(--teal)" stroke-width="4"/>
    <path d="M966 540 A13 13 0 0 1 990 532 M992 546 A13 13 0 0 1 968 554" fill="none" stroke="var(--teal)" stroke-width="5"/>
    <path d="M880 350 Q876 326 900 324 Q912 310 930 320 Q952 316 954 338 Q964 356 948 368 Q944 390 922 384 Q904 394 892 380 Q870 376 880 350Z" fill="var(--teal-light)" stroke="var(--teal)" stroke-width="4"/>
    <path d="M904 352 A14 14 0 0 1 930 344 M932 360 A14 14 0 0 1 906 368" fill="none" stroke="var(--teal)" stroke-width="5"/>
  </svg>

  <div class="studio">calmorbel</div>
</div>
</body>
</html>
```